Innovative Consulting Firm Needs New Business Cards and Stationary

Our Innovative Consulting Firm, Larkfield Consulting, is in need of new business cards and stationary designs. We want two-sided cards that incorporate our logo, which is attached. We are looking for something not too formal, but is professional and slick.

Card should have the following information:
Name (ex. Tom Bradley)
Title (ex. Manager)
Address (ex. 24680 Cedar Lane)
Address 2 (ex. Suite 100)
City
State
Zip Code
Mobile
Email

The card should also have our website: www.larkfieldconsulting.example

Industry/Entity Type

Management Consulting

Contact Information for Business Card

Name (ex. Tom Bradley)
Title (ex. Manager)
Address 2 (ex. Suite 100)
City
State
Zip Code
Mobile
Email

Font styles to use
Sans Serif

Requirements
Must have
• The colors on the card must match the colors in the logo. The exact color codes are attached in a pdf.
Nice to have
• The Company's Tagline is "Focused on your Future". This might be nice to incorporate, but not necessary.

```html
<!DOCTYPE html>
<html lang="en">
<head>
<meta charset="utf-8">
<title>Larkfield Consulting – Business Cards</title>
<link href="https://fonts.googleapis.com/css2?family=Open+Sans:wght@400;600&display=swap" rel="stylesheet">
<style>
  :root {
    --brand-blue: #1e5b94;
    --brand-blue-deep: #123f6e;
    --brand-blue-light: #2467a3;
    --brand-gold: #e8a317;
    --paper: #f6f6f6;
    --ink: #3a3a3a;
    --stage: #3b3b3d;
  }
  * { margin: 0; padding: 0; box-sizing: border-box; }
  html, body {
    width: 1200px; height: 834px; overflow: hidden;
    background: var(--stage);
    font-family: "Open Sans", Arial, sans-serif;
  }
  .canvas {
    position: relative; width: 1200px; height: 834px;
    display: flex; align-items: center; justify-content: center; gap: 60px;
  }
  .card {
    position: relative; width: 500px; height: 286px; overflow: hidden;
    box-shadow: 0 10px 30px rgba(0,0,0,.45);
  }
  .card--front {
    background: radial-gradient(ellipse at 60% 60%, var(--brand-blue-light), var(--brand-blue-deep));
    display: flex; align-items: center; justify-content: center;
  }
  .brand-name {
    display: flex; align-items: center; gap: 10px;
    font-weight: 600; font-size: 30px; letter-spacing: .5px; white-space: nowrap;
  }
  .brand-name__mark { width: 16px; height: 16px; background: var(--brand-gold); }
  .card--front .brand-name { color: #ffffff; }
  .card--back { background: var(--paper); }
  .card--back .brand-name {
    position: absolute; left: 24px; top: 140px;
    font-size: 19px; color: var(--brand-blue); gap: 8px;
  }
  .card--back .brand-name__mark { width: 11px; height: 11px; }
  .wave { position: absolute; inset: 0; }
  .contact {
    position: absolute; left: 244px; top: 24px; color: var(--ink);
    font-size: 10.5px; line-height: 1.45; white-space: nowrap;
  }
  .contact__name { color: var(--brand-blue); font-weight: 600; font-size: 16px; line-height: 1.2; }
  .contact__title { color: var(--brand-gold); font-size: 12px; margin-bottom: 8px; }
  .contact__row { display: flex; align-items: center; gap: 7px; }
  .contact__row svg { width: 10px; height: 10px; flex: none; }
  .contact__address { margin-bottom: 2px; }
</style>
</head>
<body>
<main class="canvas">
  <section class="card card--front" aria-label="Card front">
    <div class="brand-name"><span class="brand-name__mark"></span>Larkfield Consulting</div>
  </section>

  <section class="card card--back" aria-label="Card back">
    <svg class="wave" viewBox="0 0 500 286" preserveAspectRatio="none" aria-hidden="true">
      <path d="M0 250 C140 252 250 238 330 196 C385 166 435 152 500 148 L500 160 C435 164 390 178 340 206 C260 250 150 266 0 266 Z" fill="var(--brand-gold)"/>
      <path d="M0 269 C150 269 262 254 344 210 C394 182 436 170 500 164 L500 286 L0 286 Z" fill="var(--brand-blue)"/>
    </svg>
    <div class="brand-name"><span class="brand-name__mark"></span>Larkfield Consulting</div>
    <div class="contact">
      <p class="contact__name">Tom Bradley</p>
      <p class="contact__title">Manager</p>
      <p class="contact__address">24680 Cedar Lane, Suite 11<br>Brookhaven, Oregon 97035</p>
      <p class="contact__row">
        <svg viewBox="0 0 12 12"><rect x="3" y="0.5" width="6" height="11" rx="1" fill="none" stroke="var(--brand-gold)" stroke-width="1.2"/></svg>
        (555) 014-2290
      </p>
      <p class="contact__row">
        <svg viewBox="0 0 12 12"><rect x="0.6" y="2" width="10.8" height="8" fill="none" stroke="var(--brand-gold)" stroke-width="1.2"/><path d="M1 2.5 L6 6.5 L11 2.5" fill="none" stroke="var(--brand-gold)" stroke-width="1.2"/></svg>
        email@larkfieldconsulting.example
      </p>
    </div>
  </section>
</main>
</body>
</html>
```